Gentle Cradle Pregnancy and Baby Massage

I need a web design for a new business, GENTLE CRADLE PREGNANCY AND BABY MASSAGE that I am in the process of setting up in the suburbs of Perth, Western Australia. The business is owned and operated by myself and my intention is to service Pregnant Mothers and Parents of Young Babies that would benefit from massage. I would like to have a "Home Page" and pages for "About Me", "Pregnancy Massage", "Baby Massage", a Pricing Page for Pregnancy Massage Sessions, a Pricing Page for Baby Massage Sessions, and a "Contact Me" page to allow clients to either contact me with queries or book available pregnancy massage sessions on a particular day of the week. I would also like a "News" page that would include articles I have written, news about new courses and a link to my Chatterlink page (yet to be set up). I would like to keep the colour schemes similar to my logo design colours. I need the design to be easy to follow and to appeal to a younger audience (20's to mid 30's).
The target audience is pregnant mothers-to-be wishing to receive massage treatments, and new parents and grandparents of small babies that would like to learn how to massage their babies.
The look and feel should be modern, professional, elegant and feminine.
I need the design to be in a standard format such that I can update the content by myself ( and does not need specialised software) as the company and business progresses.

Target Market(s)

Contact Information for Business Card

Card should have rounded edges. Design should have the same "feel" as the website. Contact Details of my business address, mobile phone, email and website should be included.

Requirements
Must have
• Same colours as logo design. In cmyk system, the colours are: 20,60,0,0 which best result is pantone 681 and 40,40,0,0 which best result is pantone 2645. Card should include the logo design.

```html
<!DOCTYPE html>
<html lang="en">
<head>
<meta charset="utf-8">
<title>Gentle Cradle Pregnancy and Baby Massage – Benefits of Pregnancy Massage</title>
<link rel="stylesheet" href="https://fonts.googleapis.com/css2?family=Annie+Use+Your+Telescope&family=Delius&family=Patrick+Hand&family=Sorts+Mill+Goudy&display=swap">
<style>
  :root {
    --backdrop: #141414;
    --page: #efe4e5;
    --teal: #93bab7;
    --teal-dark: #6ea39f;
    --teal-pale: #c7dcda;
    --rule: #9aa3a5;
    --pink: #e0509e;
    --lavender: #a58fd6;
    --ink: #2a2326;
    --grey-band: #dcdcdc;
  }
  * { box-sizing: border-box; margin: 0; padding: 0; }
  html, body { width: 1200px; height: 1025px; overflow: hidden; background: var(--backdrop); }
  .page {
    position: absolute; left: 362px; top: 0; width: 500px; height: 1025px;
    background: var(--page); overflow: hidden;
    font-family: "Sorts Mill Goudy", Georgia, serif; color: var(--ink);
  }
  .site-header {
    position: absolute; left: 12px; top: 2px; width: 475px; height: 58px;
    background: var(--teal); border-bottom: 3px solid var(--rule);
  }
  .menu-icon { position: absolute; left: 17px; top: 18px; }
  .search-icon { position: absolute; right: 26px; top: 14px; }
  .brand {
    position: absolute; left: 50%; top: 8px; transform: translateX(-50%);
    text-align: center; color: var(--pink); font-family: "Delius", cursive; white-space: nowrap;
  }
  .brand-mark { display: block; width: 14px; height: 14px; border-radius: 50%; background: var(--pink); margin: 0 auto 2px; }
  .brand-name { font-size: 15px; line-height: 17px; }
  .brand-tag { font-size: 6px; line-height: 8px; }
  .breadcrumb {
    position: absolute; left: 43px; top: 79px; width: 162px; height: 18px;
    background: var(--teal-pale); border: 1px solid var(--teal);
    font-family: "Delius", cursive; font-size: 8px; line-height: 16px;
    color: var(--teal-dark); padding-left: 7px; white-space: nowrap;
  }
  .hero { position: absolute; left: 16px; top: 114px; width: 467px; height: 207px; background: #f1eef2; }
  .hero-photo {
    position: absolute; left: 0; top: 0; width: 246px; height: 207px;
    background: linear-gradient(100deg, #2a2323 0%, #4a3b3a 45%, #8a7270 70%, #c9b8b6 100%);
  }
  .hero-copy { position: absolute; left: 244px; top: 28px; width: 220px; text-align: center; }
  .hero-title { font-family: "Annie Use Your Telescope", cursive; font-weight: 400; color: var(--lavender); font-size: 20px; line-height: 24px; }
  .hero-text { font-family: "Patrick Hand", cursive; font-size: 17px; line-height: 19.5px; margin-top: 4px; white-space: nowrap; }
  .hero-source { font-family: "Delius", cursive; font-size: 5.5px; margin-top: 14px; padding-left: 30px; white-space: nowrap; }
  .benefits { position: absolute; left: -6px; top: 349px; width: 494px; height: 326px; }
  .benefits-photo {
    position: absolute; inset: 0;
    background: linear-gradient(180deg, #f3ecee 0%, #eadcd8 35%, #e2c6b7 65%, #efe8e6 100%);
  }
  .benefits-title {
    position: absolute; top: 0; width: 100%; text-align: center; white-space: nowrap;
    font-family: "Annie Use Your Telescope", cursive; font-weight: 400; color: var(--lavender); font-size: 24px; padding-left: 30px;
  }
  .benefits-lead {
    position: absolute; top: 28px; left: 66px; white-space: nowrap;
    font-family: "Annie Use Your Telescope", cursive; font-weight: 400; color: var(--teal-dark); font-size: 18.5px;
  }
  .benefit-list { position: absolute; left: 37px; top: 86px; width: 240px; list-style: none; font-size: 11.6px; line-height: 14.4px; }
  .benefit-list li::before { content: "•"; margin: 0 6px 0 2px; }
  .safety { position: absolute; left: 0; top: 675px; width: 500px; height: 280px; background: var(--grey-band); }
  .safety-title {
    position: absolute; left: 75px; top: 10px; white-space: nowrap;
    font-family: "Annie Use Your Telescope", cursive; font-weight: 400; color: var(--teal-dark); font-size: 20px;
  }
  .safety-col { position: absolute; top: 52px; font-size: 10.6px; line-height: 13.7px; hyphens: auto; }
  .safety-col.left { left: 45px; width: 238px; }
  .safety-col.right { left: 305px; width: 165px; }
  .safety-col ul { list-style: none; }
  .safety-col li::before { content: "•"; margin: 0 6px 0 2px; }
  .site-footer {
    position: absolute; left: 13px; top: 956px; width: 474px; height: 52px; background: var(--teal);
    display: flex; justify-content: space-around; align-items: center;
    font-family: "Delius", cursive; font-size: 11px; color: var(--pink);
  }
</style>
</head>
<body>
<main class="page">
  <header class="site-header">
    <svg class="menu-icon" width="34" height="26" viewBox="0 0 34 26" aria-label="Menu">
      <rect x="0" y="0" width="34" height="6" rx="3" fill="var(--pink)"/>
      <rect x="0" y="10" width="34" height="6" rx="3" fill="var(--pink)"/>
      <rect x="0" y="20" width="34" height="6" rx="3" fill="var(--pink)"/>
    </svg>
    <div class="brand">
      <span class="brand-mark"></span>
      <div class="brand-name">Gentle Cradle</div>
      <div class="brand-tag">Pregnancy and Baby Massage</div>
    </div>
    <svg class="search-icon" width="32" height="32" viewBox="0 0 32 32" aria-label="Search">
      <circle cx="12" cy="12" r="9.5" fill="none" stroke="var(--pink)" stroke-width="3"/>
      <line x1="19" y1="19" x2="29" y2="29" stroke="var(--pink)" stroke-width="5" stroke-linecap="round"/>
    </svg>
  </header>

  <nav class="breadcrumb">Home &lt; Benefits of pregnancy massage</nav>

  <section class="hero">
    <div class="hero-photo" role="img" aria-label="Photo of a pregnant belly cradled by a hand"></div>
    <div class="hero-copy">
      <h1 class="hero-title">Pregnancy Massage</h1>
      <p class="hero-text">Pregnancy massage is the prenatal<br>use of massage therapy<br>to support the physiological,<br>structural and emotional<br>wellbeing of both mother and baby.</p>
      <p class="hero-source">Source: Bloomwell Prenatal Massage Institute</p>
    </div>
  </section>

  <section class="benefits">
    <div class="benefits-photo" role="img" aria-label="Faded photo of a therapist's hands massaging a client's back"></div>
    <h2 class="benefits-title">Benefits of Pregnancy Massage</h2>
    <p class="benefits-lead">Pregnancy Massage is a professional relaxation massage that:</p>
    <ul class="benefit-list">
      <li>Reduces anxiety caused by hormonal changes</li>
      <li>Improves circulation</li>
      <li>Reduces muscle aches and pain; muscle and joint conditions such as backache, shoulder and neck pain, hip pain, leg cramps, oedema and carpel tunnel</li>
      <li>Relaxes tense muscle, tones loose muscle and increases muscle flexibility.</li>
      <li>Enhances vitality and energy</li>
      <li>Reduces fatigue</li>
      <li>Enhances relaxation and improves sleep patterns as it helps to soothe and relax nervous tension</li>
      <li>Increases circulation to the skin</li>
    </ul>
  </section>

  <section class="safety">
    <h2 class="safety-title">Is Pregnancy Massage Safe?</h2>
    <div class="safety-col left">
      <p>Yes, when the massage is performed by a qualified pregnancy massage therapist, who is aware of your medical and obstetric history. It is recommended to align your massage for just after your ante natal check, so that up to date information is available.</p>
      <p>There are times when pregnancy massage is not appropriate.</p>
      <ul>
        <li>The abdomen will not be massaged during the first trimester.</li>
        <li>It is recommended to wait at least one week after amniocentesis, or any invasive procedures.</li>
        <li>If you have a history of blood clots in the legs, any vaginal bleeding, or cramping, pregnancy massage is not recommended.</li>
      </ul>
    </div>
    <div class="safety-col right">
      <p>Certain medical or obstetric conditions will require medical clearance from your obstetrician. These include;</p>
      <ul>
        <li>Unstable or high blood pressure</li>
        <li>Heart disease</li>
        <li>Placenta praevia</li>
        <li>Cervical incompetence</li>
      </ul>
    </div>
  </section>

  <footer class="site-footer">
    <span>Chatterlink</span>
    <span>Pinboardly</span>
    <span>Tweetwing</span>
    <span>Circlespace</span>
    <span>Snapframe</span>
  </footer>
</main>
</body>
</html>
```